Brightmoor Co Trade Show Flyer

We need a brochure design (8.5 x 11) Info in the design (refer to rough draft I drew on Paper): "#1 selling tool to aquire new franchisees has been video testimonials" - Martin L. Greaves, C.E.O Kolva Smoothie Franchise Testimonials - Let your franchisees do the selling for you. Franchisee testimonial: $10,000 / per Franchisee Includes: • 2 minute Video • 1 minute add for your franchise's location • Concept creation • Communication with franchisee • Travel to their location • All rental equipment • 1 round of corrections • Animated logo • Licensed music ******* For 25% Discount section (next to middle box), please put the "Venture Fairground Logo" Great to use on all your social media (USE logos and icons) • Website • Clipstream • Worklink • Friendwall • Snapframe • Chirpline • Phone calls • Emails • In person meetings Some of our clients: (use the logos I uploaded - in round boxes as in draft) LOGO (Brightmoor Franchise Testimonial) www.brightmoorstories.example (866) 555-0187

Target Market(s)

Franchise owners

Colors

Designer to choose colors to be used in the design.

Requirements

```html
<!DOCTYPE html>
<html lang="en">
<head>
<meta charset="utf-8">
<title>Brightmoor Co Trade Show Flyer</title>
<link href="https://fonts.googleapis.com/css2?family=Bebas+Neue&family=Roboto:wght@300;400;500;700;900&display=swap" rel="stylesheet">
<style>
  :root {
    --ink: #1c1c1c;
    --teal: #0aa98b;
    --paper: #f1f1f1;
    --paper-light: #fafafa;
    --ring: #555555;
    --web: #1f7ee8;
    --video: #e8141b;
    --wall: #2a5aa5;
    --snap: #d9417e;
    --mail: #e2202b;
    --chirp: #1aa6e6;
    --call: #3bb54a;
    --work: #0a6aad;
  }
  * { margin: 0; padding: 0; box-sizing: border-box; }
  html, body { width: 927px; height: 1200px; overflow: hidden; }
  body {
    position: relative;
    font-family: "Roboto", Arial, sans-serif;
    color: var(--ink);
    background: linear-gradient(160deg, var(--paper-light) 0%, var(--paper) 45%, #e9e9e9 100%);
  }
  .centered { position: absolute; left: 0; width: 927px; text-align: center; }

  .quote { top: 44px; font-size: 25px; font-weight: 500; }
  .quote-source { top: 83px; font-size: 19.5px; font-weight: 300; }
  .headline {
    top: 140px; font-family: "Bebas Neue", "Arial Narrow", sans-serif;
    font-size: 86px; line-height: 86px; letter-spacing: 1px;
  }
  .tagline { top: 230px; font-size: 26px; font-weight: 500; }

  .package {
    position: absolute; left: 237px; top: 285px; width: 456px; height: 403px;
    border: 2px solid var(--ink); padding: 30px 0 0 26px;
  }
  .package-price { color: var(--teal); font-size: 26.5px; font-weight: 500; margin-bottom: 16px; }
  .package-list { list-style: none; }
  .package-list li { font-size: 20px; font-weight: 500; height: 33.4px; line-height: 33.4px; }
  .package-list li::before { content: "• "; font-size: 15px; vertical-align: 2px; }

  .discount {
    position: absolute; left: -96px; top: 341px; width: 307px; height: 307px;
    border-radius: 50%; background: #fff;
    box-shadow: 3px 2px 0 0 var(--ring);
  }
  .discount-rate {
    position: absolute; left: 30px; top: 388px; color: var(--teal);
    font-size: 64px; font-weight: 900; line-height: 1;
  }
  .discount-label {
    position: absolute; left: 30px; top: 457px; font-size: 24px; font-weight: 700; line-height: 27px;
  }
  .partner-name {
    position: absolute; left: 32px; top: 516px; width: 140px;
    color: var(--teal); font-size: 18px; font-weight: 900; line-height: 20px;
  }

  .channels-title { top: 731px; font-size: 17px; font-weight: 500; }
  .channels { position: absolute; left: 262px; top: 764px; display: flex; gap: 12px; }
  .channel {
    width: 40px; height: 40px; border-radius: 50%;
    display: flex; align-items: center; justify-content: center;
    color: #fff; font-size: 6.5px; font-weight: 700;
  }
  .channel.web { background: var(--web); }
  .channel.video { background: var(--video); }
  .channel.wall { background: var(--wall); }
  .channel.snap { background: var(--snap); }
  .channel.mail { background: var(--mail); }
  .channel.chirp { background: var(--chirp); }
  .channel.call { background: var(--call); }
  .channel.work { background: var(--work); }

  .rule { position: absolute; height: 1.5px; background: var(--ink); }
  .rule.wide { left: 253px; top: 827px; width: 421px; }
  .rule.short { left: 348px; top: 990px; width: 231px; }

  .clients-title { top: 845px; font-size: 20px; font-weight: 500; }
  .clients { position: absolute; left: 168px; top: 880px; display: flex; gap: 27px; }
  .client {
    width: 86px; height: 86px; border-radius: 50%; background: #fff;
    box-shadow: 0 2px 4px rgba(0,0,0,0.35);
    display: flex; align-items: center; justify-content: center;
    font-size: 12.5px; font-weight: 700; color: var(--ink);
  }

  .brand-dot {
    position: absolute; left: 443px; top: 1005px; width: 42px; height: 42px;
    border-radius: 50%; background: var(--ink);
  }
  .brand-name { top: 1056px; font-size: 33px; font-weight: 900; letter-spacing: 1px; }
  .brand-sub { top: 1091px; font-size: 8px; font-weight: 700; letter-spacing: 0.3px; }
  .contact-web { top: 1108px; font-size: 19px; font-weight: 400; }
  .contact-phone { top: 1137px; font-size: 19px; font-weight: 400; }
</style>
</head>
<body>
  <p class="centered quote">"#1 selling tool to aquire new franchisees has been video testimonials"</p>
  <p class="centered quote-source">-Martin L. Greaves, C.E.O Kolva Smoothie Franchise Testimonials</p>
  <h1 class="centered headline">FRANCHISE TESTIMONIALS</h1>
  <p class="centered tagline">Let your franchisees do the selling for you</p>

  <div class="discount"></div>
  <div class="discount-rate">25%</div>
  <div class="discount-label">DISCOUNT<br>FOR</div>
  <div class="partner-name">The Venture Fairground</div>

  <section class="package">
    <h2 class="package-price">$10,000 / per Franchisee Includes:</h2>
    <ul class="package-list">
      <li>2 minute Video</li>
      <li>1 minute add for your franchise's location</li>
      <li>Concept creation</li>
      <li>Communication with franchisee</li>
      <li>Travel to their location</li>
      <li>All rental equipment</li>
      <li>1 round of corrections</li>
      <li>Animated logo</li>
    </ul>
  </section>

  <p class="centered channels-title">USE YOUR TESTIMONIALS EVERYWHERE</p>
  <div class="channels">
    <div class="channel web">
      <svg width="24" height="24" viewBox="0 0 24 24" fill="none" stroke="#fff" stroke-width="1.6">
        <circle cx="12" cy="12" r="10"/><ellipse cx="12" cy="12" rx="4.5" ry="10"/>
        <line x1="2" y1="12" x2="22" y2="12"/><line x1="4" y1="7" x2="20" y2="7"/><line x1="4" y1="17" x2="20" y2="17"/>
      </svg>
    </div>
    <div class="channel video">Clipstream</div>
    <div class="channel wall">Friendwall</div>
    <div class="channel snap">Snapframe</div>
    <div class="channel mail">
      <svg width="24" height="18" viewBox="0 0 24 18" fill="none" stroke="#fff" stroke-width="2.4">
        <rect x="2" y="2" width="20" height="14" rx="1"/><polyline points="2,3 12,10 22,3"/>
      </svg>
    </div>
    <div class="channel chirp">Chirpline</div>
    <div class="channel call">
      <svg width="22" height="22" viewBox="0 0 24 24" fill="#fff">
        <path d="M6.6 10.8a15 15 0 0 0 6.6 6.6l2.2-2.2a1 1 0 0 1 1-.25 11.4 11.4 0 0 0 3.6.57 1 1 0 0 1 1 1V20a1 1 0 0 1-1 1A17 17 0 0 1 3 4a1 1 0 0 1 1-1h3.5a1 1 0 0 1 1 1c0 1.25.2 2.45.57 3.6a1 1 0 0 1-.25 1z"/>
      </svg>
    </div>
    <div class="channel work">Worklink</div>
  </div>

  <div class="rule wide"></div>
  <p class="centered clients-title">TRUSTED BY:</p>
  <div class="clients">
    <div class="client">Tidewell</div>
    <div class="client">Gearhaus</div>
    <div class="client">Scoopery</div>
    <div class="client">DayCorner</div>
    <div class="client">Kolva</div>
  </div>
  <div class="rule short"></div>

  <div class="brand-dot"></div>
  <p class="centered brand-name">BRIGHTMOOR</p>
  <p class="centered brand-sub">— FRANCHISE TESTIMONIALS —</p>
  <p class="centered contact-web">www.brightmoorstories.example</p>
  <p class="centered contact-phone">(866) 555-0187</p>
</body>
</html>
```